Law Firm Needs Stationery Design and Business Cards

i would like some fresh new ideas for letterhead. current letterhead is attached. the bottom of the letterhead should have the same content as the bottom of the current letterhead. with the dagger (cross) symbol attached at the beginning and referenced by the two names at the top. see existing letterhead and this will make better sense.

use existing logo and content. nothing overly fancy. i like simple, classy, and refined. does not have to be same font on existing letterhead.

for envelopes, use logo and Raleigh, NC address only

Industry/Entity Type

Business

Contact Information for Business Card

Name: Gordon T. Pelling, Esq.

2846 Vesper Lane, Suite 417
Raleigh, NC 27893

phone 919-555-0143
fax 919-555-0187
cell 919-555-0162

www.pellinglegalgroup.com
gordon@pellinglegalgroup.com

```html
<!DOCTYPE html>
<html lang="en">
<head>
<meta charset="utf-8">
<title>Pelling Law – Letterhead</title>
<link rel="stylesheet" href="https://fonts.googleapis.com/css2?family=Questrial&family=Mulish:wght@400;700&display=swap">
<style>
  :root {
    --backdrop: #d6d6d6;
    --paper: #f4f4f4;
    --navy: #1b2a6b;
    --band-navy: #16246a;
    --slate: #7c7c7c;
    --ink: #555555;
    --ink-dark: #333333;
    --rule: #cfcfcf;
    --signature-tone: #c9cfe6;
  }
  * { margin: 0; padding: 0; box-sizing: border-box; }
  html, body { width: 1200px; height: 1000px; overflow: hidden; }
  body {
    background: var(--backdrop);
    position: relative;
    font-family: "Questrial", "Mulish", sans-serif;
    color: var(--ink);
  }
  .letterhead {
    position: absolute;
    left: 260px; top: 65px;
    width: 685px; height: 885px;
    background: var(--paper);
  }
  .top-bar {
    position: absolute; left: 0; top: 0; width: 100%; height: 7px;
    background: var(--slate);
  }
  .bottom-band {
    position: absolute; left: 0; bottom: 0; width: 100%; height: 11px;
    background: var(--band-navy);
  }
  .brand-disc {
    position: absolute; left: 310px; top: 68px;
    width: 64px; height: 64px; border-radius: 50%;
    background: var(--navy);
  }
  .brand-name {
    position: absolute; left: 0; top: 140px; width: 100%;
    text-align: center;
    font-family: "Questrial", sans-serif;
    font-size: 22px; letter-spacing: 2px; line-height: 26px;
    color: var(--navy);
  }
  .letter {
    position: absolute; left: 64px; top: 287px; width: 558px;
    font-size: 10.6px; line-height: 12px; letter-spacing: 0.15px;
  }
  .salutation, .signer {
    font-family: "Mulish", sans-serif; font-weight: 700; color: var(--ink-dark);
  }
  .salutation { margin-bottom: 13px; }
  .paragraph { text-align: justify; margin-bottom: 11px; }
  .closing { margin-top: 18px; }
  .signature {
    position: absolute; left: 145px; top: 572px; width: 145px; height: 76px;
    background: linear-gradient(90deg, transparent, var(--signature-tone) 20%, var(--signature-tone) 80%, transparent);
    opacity: .55; border-radius: 30px;
  }
  .contact-col {
    position: absolute; top: 803px;
    font-family: "Mulish", sans-serif;
    font-size: 9px; line-height: 10.6px; color: var(--ink);
    white-space: nowrap;
  }
  .attorney-1 { left: 44px; }
  .attorney-2 { left: 228px; }
  .office-raleigh { left: 416px; }
  .office-orlando { left: 566px; }
  .divider {
    position: absolute; top: 802px; width: 1px; height: 52px;
    background: var(--rule);
  }
  .divider.d1 { left: 214px; }
  .divider.d2 { left: 402px; }
  .divider.d3 { left: 551px; }
  .attorney-name { font-weight: 700; color: var(--navy); text-transform: uppercase; }
  .label { font-weight: 700; color: var(--navy); }
</style>
</head>
<body>
  <main class="letterhead">
    <div class="top-bar"></div>

    <header>
      <div class="brand-disc"></div>
      <div class="brand-name">PELLING LAW</div>
    </header>

    <article class="letter">
      <p class="salutation">Dear sir,</p>
      <p class="paragraph">Communication is a very integral part of living creatures, animals and humans. Communication may be verbal or written. Written communication however is only applicable to human beings. Can you even imagine a world without communication? Verbal communication can be through telephones, webcams or in person. Written communication is through letters, emails and mobile phone messages.</p>
      <p class="paragraph">In today’s world of great inventions and technology, letters have somehow become redundant. It is the time for text messages or chats. But they still can communicate a lot more than all other modes of communication. Organizations and various government departments still bank on letters as a strong medium of communication. There is no comparison in costs of sending letters as compared to costs of mobile phone messages though – letters are far cheaper. Letters now commonly known as “hard copy documents” are considered more relevant and important than email copies of text messages as proof or evidence of some sort.</p>
      <p class="paragraph">Letters speak volumes about a person or an organization that writes it. So one must take utmost care ensuring that the language used in any letter is appropriate for the occasion for which it is being written. Since a letter is also a written proof or document, if there are certain things that should not form a part of it, then that too should be carefully handled.</p>
      <p class="paragraph">Writing a good letter is an art. But if for some reason someone is unable to write that perfect letter, these different types of letters provide a base for you to build on. Sample letters have been given for everyone to understand what all information needs to form a part of the letter type and then it can be customized.</p>
      <p class="closing">Yours Sincerely,</p>
      <p class="signer">Dana Corlis</p>
    </article>

    <div class="signature" role="img" aria-label="Handwritten signature of Dana Corlis"></div>

    <footer>
      <div class="contact-col attorney-1">
        <div class="attorney-name">Gordon T. Pelling, Esq.</div>
        <div>Licensed in NC and FL</div>
        <div>Board Certified in Civil Trial Law</div>
        <div>by NBLSC and FL Bar</div>
      </div>
      <div class="divider d1"></div>
      <div class="contact-col attorney-2">
        <div class="attorney-name">Harold J. Whitcomb, Esq.</div>
        <div>Licensed in FL, GA, and NY</div>
        <div>Board Certified in Civil Trial Law</div>
        <div>by NBLSC and FL Bar</div>
      </div>
      <div class="divider d2"></div>
      <div class="contact-col office-raleigh">
        <div>2846 Vesper Lane, Suite 417</div>
        <div>Raleigh, NC 27893</div>
        <div><span class="label">T:</span> 919.555.0143</div>
        <div><span class="label">F:</span> 919.555.0187</div>
        <div>www.pellinglegalgroup.com</div>
      </div>
      <div class="divider d3"></div>
      <div class="contact-col office-orlando">
        <div>88 W. Larch Street</div>
        <div>Orlando, FL 32869</div>
        <div><span class="label">T:</span> 321.555.0129</div>
        <div><span class="label">F:</span> 919.555.0187</div>
      </div>
    </footer>

    <div class="bottom-band"></div>
  </main>
</body>
</html>
```